Manuka honey jar label for new Manuka brand

We are planning to start a Manuka honey brand and we need to design the label for the honey jar. Manuka honey is an up and coming product and the market is still young in our country.
Our market is dominated by 1 brand: Orvana Health (photo attached). To the people who know what Manuka honey is, they associate it with Orvana Health in the same way people associate Cola with Zindle Pop or printer copies with Quorvix.
The good news is that a lot of people do not know yet what Manuka honey is and we still have the opportunity of being the first brand they get to know. At the same time, we still need to be able to take at least a bite out of the Orvana Health market share.
The Orvana Health label for their jar I think is not just absolutely gorgeous but it also does its job extremely well. It only features 3 informations:
- name of brand/logo (Orvana Health)
- name of product (Manuka Honey)
- and mgo rating which is like a rating of how strong the honey is
By having just this information on a relatively small label, their label SCREAMS Manuka by having the Manuka words twice (the brand and the product name) and people develop this association between Orvana Health and Manuka products in general.
Our product will also be in a similar square plastic jar. It will also be dark tinted, that´s important to note. We can also go for a blue cap but in order to differentiate ourselves from Orvana Health we thought of maybe choosing a black lid instead. I uploaded 2 jars, 1 with black lid and 1 with gold (although it looks more like mustard) that you can use for simulations. They are pretty accurate of the type of jars and lids that we can have.
The label has total length of about 20cm. One side of the jar has 5,5 cm of the label and the height of the label is 4,5 cm. We can also use selective gold laminating on the label but we cannot have custom shape label at this point as Orvana Health does with its tree logo that sticks outside the label.
I need the design for the entire label but the focus should be on the front part, that is the part that sells and catches your eye. Like Orvana Health, the front part I want to have 3 vital informations:
- name of brand/logo (in our case Velmora Botanica) - we do not have a pre-existing logo, this needs to be created alongside the label
- and mgo rating
As "other" information we also need the net weight "250 g" alongside with the typical "e" to appear on the front. That is a legal requirement.
Optionally, you can add a small phrase somewhere like "Harvested in New Zealand" or "Made in New Zealand" since this is a product that is only made there and in some areas of Australia.
This is pretty much all the info. As a final note, there are a ton of beautiful premium Manuka honey jar labels. But they are too fancy and when you look at them you don´t instantly recognize that it is Manuka Honey.
This instant recognition is vital! With this small jar there is the danger for customers to think that maybe it´s medicine, maybe it´s sports supplements etc. This is a relatively small product and imagine you just glance on it on the retail shelf. Instantly you must think it is Manuka Honey and that it is beautiful. And if you see it on the shelf next to Orvana Health, it would be best to also think that you would rather buy this (it gives you more trust) than the Orvana Health.
One final note: I do not want the bee as an insect on the label. I think some people are turned off when they see an insect with its small legs and make a bad association that there are insects inside. I do not mind symbolism or somehow super stylized bee in a modern way, but I do not want a plain insect on the label.
For any other questions, I am at your disposal. Thank you very much for taking the time to send us a proposal!

```html
<!DOCTYPE html>
<html lang="en">
<head>
<meta charset="UTF-8">
<title>Velmora Botanica Manuka Honey – Label Range</title>
<link href="https://fonts.googleapis.com/css2?family=Red+Hat+Display:wght@500;600;700;800&display=swap" rel="stylesheet">
<style>
  :root{
    --page:#ececea;
    --red:#b8202b;
    --blue:#1d3d8a;
    --green:#136635;
    --gold:#e6b53d;
    --gold-deep:#c8922a;
    --white:#ffffff;
    --ink:#2a2a2a;
    --label-w:330px;
    --label-h:270px;
  }
  *{box-sizing:border-box;margin:0;padding:0}
  html,body{width:1200px;height:675px;overflow:hidden}
  body{
    background:var(--page);
    font-family:"Red Hat Display",sans-serif;
    display:flex;align-items:center;justify-content:center;gap:40px;
  }
  .label{
    width:var(--label-w);height:var(--label-h);
    display:flex;flex-direction:column;
    border-radius:4px;overflow:hidden;
    box-shadow:0 6px 18px rgba(0,0,0,.12);
  }
  .label--red{--tone:var(--red)}
  .label--blue{--tone:var(--blue)}
  .label--green{--tone:var(--green)}

  .label__field{
    position:relative;flex:0 0 200px;
    background:var(--tone);
    display:flex;flex-direction:column;align-items:center;
  }
  .label__pattern{
    position:absolute;inset:0;
    background:linear-gradient(180deg,rgba(0,0,0,.06),rgba(0,0,0,.12));
  }
  .brand-badge{
    position:relative;width:164px;height:92px;
    display:flex;flex-direction:column;align-items:center;justify-content:center;
    padding-bottom:12px;
  }
  .brand-badge svg{position:absolute;inset:0}
  .brand-badge__name{
    position:relative;
    color:var(--gold);font-weight:700;font-size:22px;line-height:1.05;text-align:center;
  }
  .product-name{
    position:relative;margin-top:14px;
    color:var(--white);font-weight:600;font-size:37px;letter-spacing:-.3px;line-height:1;
  }
  .origin{
    position:relative;margin-top:12px;width:272px;
    border-top:1.5px solid var(--white);border-bottom:1.5px solid var(--white);
    padding:9px 0 8px;text-align:center;
    color:var(--white);font-weight:800;font-size:11px;letter-spacing:2.6px;
  }
  .label__band{flex:0 0 5px;background:linear-gradient(90deg,var(--gold-deep),var(--gold),var(--gold-deep))}
  .label__base{
    flex:1;background:var(--white);
    display:flex;align-items:center;justify-content:space-between;padding:0 26px 0 28px;
  }
  .mgo{position:relative;width:76px;height:38px;display:flex;align-items:center;justify-content:center}
  .mgo svg{position:absolute;inset:0}
  .mgo__text{position:relative;color:var(--white);font-weight:600;font-size:12px}
  .net{color:var(--ink);font-weight:600;font-size:15px}
</style>
</head>
<body>

<section class="label label--red" aria-label="Velmora Botanica Manuka Honey label, red">
  <div class="label__field">
    <div class="label__pattern" role="img" aria-label="Subtle tone-on-tone floral pattern"></div>
    <div class="brand-badge">
      <svg viewBox="0 0 164 92" aria-hidden="true"><polyline points="3,0 3,44 56,88 108,88 161,44 161,0" fill="var(--tone)" stroke="var(--gold)" stroke-width="2.5"/></svg>
      <span class="brand-badge__name">Velmora<br>Botanica</span>
    </div>
    <h1 class="product-name">Manuka Honey</h1>
    <p class="origin">MADE IN NEW ZEALAND</p>
  </div>
  <div class="label__band"></div>
  <div class="label__base">
    <div class="mgo">
      <svg viewBox="0 0 76 38" aria-hidden="true"><polygon points="10,1 28,1 38,19 28,37 10,37 0,19" fill="var(--tone)"/><polygon points="48,1 66,1 76,19 66,37 48,37 38,19" fill="var(--tone)"/><rect x="20" y="5" width="36" height="28" fill="var(--tone)"/></svg>
      <span class="mgo__text">MGO° 250</span>
    </div>
    <span class="net">℮ 250g</span>
  </div>
</section>

<section class="label label--blue" aria-label="Velmora Botanica Manuka Honey label, blue">
  <div class="label__field">
    <div class="label__pattern" role="img" aria-label="Subtle tone-on-tone floral pattern"></div>
    <div class="brand-badge">
      <svg viewBox="0 0 164 92" aria-hidden="true"><polyline points="3,0 3,44 56,88 108,88 161,44 161,0" fill="var(--tone)" stroke="var(--gold)" stroke-width="2.5"/></svg>
      <span class="brand-badge__name">Velmora<br>Botanica</span>
    </div>
    <h1 class="product-name">Manuka Honey</h1>
    <p class="origin">MADE IN NEW ZEALAND</p>
  </div>
  <div class="label__band"></div>
  <div class="label__base">
    <div class="mgo">
      <svg viewBox="0 0 76 38" aria-hidden="true"><polygon points="10,1 28,1 38,19 28,37 10,37 0,19" fill="var(--tone)"/><polygon points="48,1 66,1 76,19 66,37 48,37 38,19" fill="var(--tone)"/><rect x="20" y="5" width="36" height="28" fill="var(--tone)"/></svg>
      <span class="mgo__text">MGO° 250</span>
    </div>
    <span class="net">℮ 250g</span>
  </div>
</section>

<section class="label label--green" aria-label="Velmora Botanica Manuka Honey label, green">
  <div class="label__field">
    <div class="label__pattern" role="img" aria-label="Subtle tone-on-tone floral pattern"></div>
    <div class="brand-badge">
      <svg viewBox="0 0 164 92" aria-hidden="true"><polyline points="3,0 3,44 56,88 108,88 161,44 161,0" fill="var(--tone)" stroke="var(--gold)" stroke-width="2.5"/></svg>
      <span class="brand-badge__name">Velmora<br>Botanica</span>
    </div>
    <h1 class="product-name">Manuka Honey</h1>
    <p class="origin">MADE IN NEW ZEALAND</p>
  </div>
  <div class="label__band"></div>
  <div class="label__base">
    <div class="mgo">
      <svg viewBox="0 0 76 38" aria-hidden="true"><polygon points="10,1 28,1 38,19 28,37 10,37 0,19" fill="var(--tone)"/><polygon points="48,1 66,1 76,19 66,37 48,37 38,19" fill="var(--tone)"/><rect x="20" y="5" width="36" height="28" fill="var(--tone)"/></svg>
      <span class="mgo__text">MGO° 250</span>
    </div>
    <span class="net">℮ 250g</span>
  </div>
</section>

</body>
</html>
```